Need business card design
Velin Medical
Simple
Tobias Morvel
CEO
12345 any street
city, state 98765
tmorvel@velinmedical.net
www.velinmedical.net
Just looking for design for now. Additional info will be added later

```html
<!DOCTYPE html>
<html lang="en">
<head>
<meta charset="utf-8">
<title>Velin Medical – Business Card</title>
<link href="https://fonts.googleapis.com/css2?family=Arimo:wght@400;700&display=swap" rel="stylesheet">
<style>
  :root {
    --stage: #000000;
    --frame: #ffffff;
    --slate: #4a5a6d;
    --green: #3cae49;
    --white: #ffffff;
    --paper: #ffffff;
  }
  * { margin: 0; padding: 0; box-sizing: border-box; }
  html, body { width: 1200px; height: 883px; overflow: hidden; background: var(--frame); }
  body { font-family: "Arimo", Arial, sans-serif; }
  .stage {
    position: absolute; left: 10px; top: 10px; width: 1180px; height: 863px;
    background: var(--stage);
  }
  .card { position: absolute; overflow: hidden; }
  .card-front {
    left: 331px; top: 67px; width: 575px; height: 331px;
    background: var(--slate);
  }
  .brand {
    position: absolute; display: flex; align-items: center; gap: 14px;
    font-weight: 700; white-space: nowrap;
  }
  .brand-mark { width: 26px; height: 26px; background: var(--green); flex: none; }
  .card-front .brand { left: 140px; top: 130px; font-size: 52px; color: var(--white); }
  .front-web {
    position: absolute; left: 0; right: 0; top: 282px; text-align: center;
    font-size: 9px; color: var(--green); letter-spacing: 0.5px;
  }
  .card-back {
    left: 331px; top: 484px; width: 583px; height: 331px;
    display: flex;
  }
  .back-brand-side { width: 290px; height: 100%; background: var(--paper); position: relative; }
  .card-back .brand { left: 18px; top: 140px; font-size: 34px; color: var(--slate); gap: 10px; }
  .card-back .brand-mark { width: 20px; height: 20px; }
  .back-info {
    flex: 1; height: 100%; background: var(--slate); color: var(--white);
    padding: 40px 0 0 24px;
  }
  .person-name { font-size: 31px; font-weight: 700; line-height: 1.1; }
  .person-role { font-size: 28px; line-height: 1.2; margin-bottom: 30px; }
  .address { font-size: 16px; line-height: 1.3; margin-bottom: 14px; }
  .contacts { font-size: 16px; line-height: 1.25; }
  .contacts div { display: flex; }
  .contacts dt { width: 12px; font-weight: 700; }
  .contacts dd { padding-left: 100px; }
  .contacts .email dd { padding-left: 16px; }
</style>
</head>
<body>
  <div class="stage">
    <section class="card card-front">
      <div class="brand"><span class="brand-mark"></span>Velin Medical</div>
      <div class="front-web">www.velinmedical.net</div>
    </section>

    <section class="card card-back">
      <div class="back-brand-side">
        <div class="brand"><span class="brand-mark"></span>Velin Medical</div>
      </div>
      <div class="back-info">
        <div class="person-name">Tobias Morvel</div>
        <div class="person-role">CEO</div>
        <div class="address">12345 Any Street,<br>Alder Creek, CA 98765</div>
        <dl class="contacts">
          <div><dt>p:</dt><dd>(123) 456 7890</dd></div>
          <div><dt>c:</dt><dd>(123) 456 7890</dd></div>
          <div><dt>f:</dt><dd>(123) 456 7890</dd></div>
          <div class="email"><dt>e:</dt><dd>tmorvel@velinmedical.net</dd></div>
        </dl>
      </div>
    </section>
  </div>
</body>
</html>
```